Menu Board that is editable in Canva (NO AI).

I am looking for help creating a simple, highly readable menu system for **Fickle Buns**, a scratch-made bakery concept centered around large rolls that customers can order simply or customize.

The overall design should feel **playful, unexpected, slightly quirky, and full of personality without feeling juvenile, chaotic, or difficult to read**.

I want the menu to be fun and memorable, but the ordering system itself needs to be extremely easy to understand at a glance.

## Brand Personality

Fickle Buns balances two sides:

**Fickle** = playful, imperfect, unexpected, expressive, slightly weird, and willing to break the rules.

**Rolls** = familiar, dependable, scratch-made, comforting, and approachable.

The food is taken seriously, but the brand should not take itself too seriously.

The menu should reflect that balance. I would like personality to come through in typography, graphic elements, shapes, illustrations, imperfect details, and subtle graffiti or hand-drawn influences rather than making the information itself chaotic.

## Typography

The two primary fonts will be:

**Oleo Ugly**
Used selectively for personality, large headlines, category names, featured words, or graphic accents.

**Montserrat**
Used for descriptions, prices, ingredients, instructions, and anything that needs to be read quickly.

Oleo Ugly should provide the playful, slightly unpredictable **Fickle** element, while Montserrat keeps the menu grounded, organized, and functional.

## Brand Color Palette

The Fickle Buns color palette is:

**Crimson Ink**
#8B162B

**Dusty Rose**
#F9B6B8

**Cosmic Latte**
#F6F3CF

**Neon Pear**
#C6B63B

**Burnt Sienna**
#F37521

**Arctic Blue**
#BAD2E8

These colors are intended to work as a flexible brand system rather than all being used equally on every piece.

For the **Ember Lineup**, I envision leaning primarily into:

* Crimson Ink
* Cosmic Latte
* Burnt Sienna
* Neon Pear

The overall Fickle Buns palette should remain recognizable, while seasonal menus can emphasize different combinations of colors.

I would like the colors to feel bold and slightly unexpected rather than traditionally rustic or “fall farmhouse.” The Harvest menu can feel warm and seasonal without relying heavily on brown, muted orange, wood grain, or other conventional autumn design elements.

## Menu Structure

The ordering system has three primary categories:

### GO CLASSIC — $6

Customers choose:

* One roll
* One icing

### GO SIGNATURE — $7

Customers choose one of our pre-designed seasonal Signature Rolls.

These are curated seasonal combinations created by us and will change throughout the year.

### GO FICKLE — $7

Customers build their own roll by choosing:

* One roll
* One icing
* One filling
* One drizzle
* One crunch

The most important design goal is that a customer should be able to look at the menu and understand these three ordering options almost immediately.

## Pick Your Roll

The three Fickle Buns bases are:

### CLASSIC CINNAMON ROLL

Soft, fluffy and unapologetically classic, with our signature cinnamon filling.

### CARAMEL ROLL

Soft, buttery and caramel-forward with no cinnamon, so the other flavors get to shine.

### SOURDOUGH CINNAMON ROLL

Our classic cinnamon roll with the deeper flavor and character of sourdough.

These descriptions should be visible but secondary to the roll names. The customer should first see the three choices, then be able to quickly understand what makes each one different.

## Pick Your Icing

### CLASSIC BUTTERCREAM

The one that started it all. Rich, silky, buttery-sweet, and generously decadent.

### CREAM CHEESE ICING

The Brantmoor Classic. Thick, creamy, tangy, and perfectly sweet with that unmistakable cream cheese finish.

### VANILLA SWEET CREAM ICING

Light, fluffy, and silky with a soft vanilla sweetness. Think whipped cream meets icing: airy, creamy, and made to melt right into your roll.

The icing names should remain easy to scan, with the descriptions present as supporting information rather than dominating the layout.

## Ember Lineup

The first seasonal menu will be the **Ember Lineup**, running September through November.

The available finishes will remain mostly consistent throughout the Harvest season, while the featured Signature Rolls can change monthly.

## September Signature Rolls

### CARAMEL APPLE

Classic Cinnamon Roll
Cream Cheese Icing
Apple
Caramel
Shortbread Crumble

### BROWNIE SUNDAE

Caramel Roll
Vanilla Sweet Cream Icing
Chocolate Brownie
Chocolate Ganache
Salted Peanuts

### CRUMBELLE COOKIE CRUNCH

Sourdough Cinnamon Roll
Classic Buttercream
Crumbelle Cookie Butter
Browned Butter Glaze
Crumbelle Cookie Crumbles

The Signature Rolls should be one of the most visually appealing parts of the menu. These are combinations we have already designed for the customer, so they should feel easy to order and tempting at a glance.

## Go Fickle Finish Categories

Customers choosing **Go Fickle** select one option from each finishing category.

### ICING

* Classic Buttercream
* Cream Cheese Icing
* Vanilla Sweet Cream Icing

### FILLING

* Apple
* Pumpkin
* Chocolate Brownie
* Coconut Pecan
* Crumbelle Cookie Butter

### DRIZZLE

* Classic Butter Glaze
* Browned Butter Glaze
* Caramel
* Espresso Glaze
* Coconut Glaze
* Chocolate Ganache

### CRUNCH

* Shortbread Crumble
* Salted Peanuts
* Chocolate Espresso Beans
* Crumbelle Cookie Crumbles
* Toasted Coconut
* Candied Pecans
* Graham Cracker Crumbs

The four finishing categories should be visually distinct and easy to follow in order:

**Icing → Filling → Drizzle → Crunch**

The customer should immediately understand that they choose **one from each category**.

## Physical Menu Format

Space is limited and the menu will be suspended from the ceiling behind the counter.

The individual menu pieces will be approximately **8.5 × 11 landscape**, mounted to a lightweight rigid backing and hung as coordinated signs.

I currently envision approximately three menu boards:

### Board 1 — How Do You Roll?

A simple introduction to the three ways to order:

**Go Classic — $6**
Roll + Icing

**Go Signature — $7**
Choose one of our seasonal Signature Rolls

**Go Fickle — $7**
Roll + Icing + Filling + Drizzle + Crunch

This board should be extremely simple and readable from a distance.

### Board 2 — Go Classic + September Signatures

One portion of the board should show the three roll choices and three icing choices, including their short descriptions.

The other portion should feature the current September Signature Rolls.

### Board 3 — Go Fickle

This board should show:

**Pick Your Roll**

followed by four clearly organized finishing categories:

**Icing | Filling | Drizzle | Crunch**

This board contains the most information and should therefore have the strongest visual organization and the least unnecessary decoration.

## Design Direction

I would like the finished menu to feel:

* Playful
* Slightly unconventional
* Modern with handmade personality
* Bold
* Fun
* Friendly
* Approachable
* Easy to scan quickly
* Organized
* Adult and intentional rather than childish

I am interested in selective influences from **graffiti, hand-drawn graphics, paint marks, arrows, stars, doodles, imperfect lines, unexpected shapes, and layered typography**.

However, these elements should support the menu rather than interfere with readability.

I do not want the design to feel like a children's menu, overly rustic, overly polished or corporate, or visually chaotic.

Because the menu will hang overhead and customers will often read it from several feet away, **clarity and hierarchy are more important than fitting in extra decoration**.

The overall philosophy for the design is:

**The branding gets to misbehave.
The information does not.**

A customer should quickly understand:

**Go Classic** = keep it simple.
**Go Signature** = choose one of ours.
**Go Fickle** = build your own.

The final result should feel distinctive enough that someone immediately recognizes Fickle Buns has personality, while being simple enough that ordering requires almost no explanation from staff.

Target Market(s)

People who enjoy treats

Industry/Entity Type

Bakery

Requirements
Must have
• Simplicity to understand
Should not have
• No AI, No stock photos.

```html
<!DOCTYPE html>
<html lang="en">
<head>
<meta charset="utf-8">
<title>Fickle Buns — How Do You Roll?</title>
<link href="https://fonts.googleapis.com/css2?family=Montserrat:wght@500;600;700;800&family=Oleo+Script:wght@400;700&family=Titan+One&family=Gochi+Hand&display=swap" rel="stylesheet">
<style>
  :root{
    --crimson:#8B162B;
    --rose:#F9B6B8;
    --latte:#F6F3CF;
    --pear:#C6B63B;
    --pear-deep:#857A32;
    --sienna:#F37521;
    --sienna-soft:#F7A24F;
    --arctic:#BAD2E8;
    --ink:#1E1A1A;
    --white:#FFFFFF;
  }
  *{box-sizing:border-box;margin:0;padding:0}
  html,body{width:1200px;height:927px;overflow:hidden;background:var(--latte)}
  .board{position:relative;width:1200px;height:927px;background:var(--latte);overflow:hidden;font-family:"Montserrat",sans-serif}

  .headline-kicker{position:absolute;left:178px;top:40px;font-family:"Gochi Hand",cursive;font-size:80px;line-height:1;letter-spacing:2px;white-space:nowrap}
  .headline-kicker .how{color:var(--sienna-soft)}
  .headline-kicker .do{color:var(--rose)}
  .headline-kicker .you{color:var(--pear)}
  .headline-main{position:absolute;left:66px;top:128px;font-family:"Titan One",sans-serif;font-size:146px;line-height:1;color:var(--crimson);letter-spacing:-2px;transform:rotate(-3deg);transform-origin:left center;white-space:nowrap}
  .headline-underline{position:absolute;left:362px;top:268px;width:262px;height:26px}

  .hero-photo{position:absolute;left:752px;top:8px;width:430px;height:350px;border-radius:48% 52% 45% 55%;background:radial-gradient(circle at 45% 45%,#C9692A 0%,#B0531F 45%,rgba(246,243,207,0) 72%)}

  .menu-card{position:absolute;background:var(--white);border-radius:10px;box-shadow:0 4px 10px rgba(60,30,20,.18);text-align:center}
  .card-flag{position:absolute;left:0;top:0;height:88px;display:flex;align-items:center;padding-left:34px;font-family:"Oleo Script",sans-serif;font-weight:700;font-size:62px;color:var(--white);clip-path:polygon(0 0,100% 0,86% 50%,100% 100%,0 100%)}
  .price-badge{position:absolute;width:100px;height:100px;border-radius:50%;background:var(--white);border:2px solid currentColor;display:flex;align-items:center;justify-content:center;font-weight:800;font-size:44px;box-shadow:0 2px 6px rgba(0,0,0,.12)}
  .card-title{font-weight:800;line-height:1}
  .card-tagline{font-weight:600;font-size:11px;letter-spacing:1.6px;color:var(--ink);margin-top:10px}
  .card-divider{display:flex;align-items:center;justify-content:center;gap:4px;margin:12px auto 0;width:64%}
  .card-divider span{flex:1;height:1.5px;background:currentColor}
  .card-divider svg{width:10px;height:10px}
  .card-art{margin:14px auto 0;border-radius:8px}
  .card-band{position:absolute;left:0;right:0;bottom:0;color:var(--white);font-weight:700;display:flex;align-items:center;justify-content:center;padding-top:20px;line-height:1.25}
  .card-band svg{position:absolute;left:0;top:-1px;width:100%;height:22px}

  .card-classic{left:50px;top:420px;width:356px;height:420px;transform:rotate(-3deg);color:var(--crimson)}
  .card-classic .card-flag{width:176px;background:var(--crimson)}
  .card-classic .price-badge{right:-6px;top:-14px}
  .card-classic .card-body{padding-top:116px}
  .card-classic .card-title{font-size:44px}
  .card-classic .card-art{width:220px;height:80px;background:linear-gradient(90deg,#E9CFD3,#F4E3E6)}
  .card-classic .card-band{height:78px;background:var(--crimson);font-size:23px}

  .card-signature{left:434px;top:326px;width:334px;height:412px;color:var(--sienna)}
  .card-signature .card-flag{width:172px;background:var(--sienna);top:0;border-radius:10px 0 0 0}
  .card-signature .price-badge{right:-20px;top:-22px;width:104px;height:104px;font-size:46px}
  .card-signature .card-body{padding-top:108px}
  .card-signature .card-title{font-size:40px}
  .card-signature .card-tagline{margin-top:8px}
  .card-signature .card-art{width:160px;height:84px;background:linear-gradient(180deg,#FCE6D3,#F8D3B4)}
  .card-signature .card-lead{font-weight:600;font-size:12px;color:var(--ink);margin-top:10px}
  .card-signature .card-band{height:92px;background:var(--sienna);font-size:22px;border-radius:0 0 10px 10px}

  .card-fickle{left:782px;top:416px;width:346px;height:450px;transform:rotate(4deg);color:var(--pear-deep)}
  .card-fickle .card-flag{width:176px;background:var(--pear-deep)}
  .card-fickle .price-badge{right:-12px;top:-6px}
  .card-fickle .card-body{padding-top:120px}
  .card-fickle .card-title{font-size:44px}
  .card-fickle .card-art{width:250px;height:110px;background:linear-gradient(90deg,#ECE9D0,#F3F1DF)}
  .card-fickle .card-band{height:108px;background:var(--pear-deep);font-size:20px}

  .brand-name{position:absolute;left:478px;top:800px;width:210px;text-align:center;font-family:"Montserrat",sans-serif;font-weight:800;font-size:34px;line-height:1.05;color:var(--crimson)}
</style>
</head>
<body>
<main class="board">

  <div class="headline-kicker"><span class="how">HOW</span> <span class="do">DO</span> <span class="you">YOU</span></div>
  <h1 class="headline-main">ROLLS?</h1>
  <svg class="headline-underline" viewBox="0 0 262 26" aria-hidden="true">
    <path d="M4 22 C80 12 170 6 258 4" stroke="var(--crimson)" stroke-width="5" fill="none" stroke-linecap="round"/>
    <path d="M40 14 C110 8 190 6 256 8" stroke="var(--crimson)" stroke-width="3" fill="none" stroke-linecap="round"/>
  </svg>

  <div class="hero-photo" role="img" aria-label="Photo of three sugar-topped cinnamon rolls with scattered crumbs"></div>

  <section class="menu-card card-classic">
    <div class="card-flag">GO</div>
    <div class="price-badge">$6</div>
    <div class="card-body">
      <h2 class="card-title">CLASSIC</h2>
      <p class="card-tagline">SIMPLE. SWEET. ALWAYS A HIT</p>
      <div class="card-divider"><span></span><svg viewBox="0 0 10 10"><path d="M5 9 L1 5 A2.2 2.2 0 0 1 5 2 A2.2 2.2 0 0 1 9 5 Z" fill="currentColor"/></svg><span></span></div>
      <div class="card-art" role="img" aria-label="Sketch of a roll plus a swirl of icing"></div>
    </div>
    <div class="card-band">
      <svg viewBox="0 0 100 20" preserveAspectRatio="none" aria-hidden="true"><path d="M0 0 H100 V8 C85 2 70 14 50 8 C30 2 15 14 0 8 Z" fill="var(--white)"/></svg>
      ROLL + ICING
    </div>
  </section>

  <section class="menu-card card-signature">
    <div class="card-flag">GO</div>
    <div class="price-badge">$7</div>
    <div class="card-body">
      <h2 class="card-title">SIGNATURE</h2>
      <p class="card-tagline">BOLD FLAVOR . MADE FOR YOU</p>
      <div class="card-divider"><span></span><svg viewBox="0 0 10 10"><path d="M5 9 L1 5 A2.2 2.2 0 0 1 5 2 A2.2 2.2 0 0 1 9 5 Z" fill="currentColor"/></svg><span></span></div>
      <div class="card-art" role="img" aria-label="Sketch of a single cinnamon roll"></div>
      <p class="card-lead">CHOOSE ONE OF OUR</p>
    </div>
    <div class="card-band">
      <svg viewBox="0 0 100 20" preserveAspectRatio="none" aria-hidden="true"><path d="M0 0 H100 V8 C85 2 70 14 50 8 C30 2 15 14 0 8 Z" fill="var(--white)"/></svg>
      SEASONAL<br>SIGNATURE ROLL
    </div>
  </section>

  <section class="menu-card card-fickle">
    <div class="card-flag">GO</div>
    <div class="price-badge">$7</div>
    <div class="card-body">
      <h2 class="card-title">FICKLE</h2>
      <p class="card-tagline">BOLD. LOADED.UNAPOLOGETIC</p>
      <div class="card-divider"><span></span><svg viewBox="0 0 10 10"><path d="M5 9 L1 5 A2.2 2.2 0 0 1 5 2 A2.2 2.2 0 0 1 9 5 Z" fill="currentColor"/></svg><span></span></div>
      <div class="card-art" role="img" aria-label="Sketches of roll, icing, drizzle jar, filling and crunch toppings joined by plus signs"></div>
    </div>
    <div class="card-band">
      <svg viewBox="0 0 100 20" preserveAspectRatio="none" aria-hidden="true"><path d="M0 0 H100 V8 C85 2 70 14 50 8 C30 2 15 14 0 8 Z" fill="var(--white)"/></svg>
      ROLL+ ICING + FILLING<br>+DRIZZLE+ CRUNCH
    </div>
  </section>

  <div class="brand-name">Fickle<br>Buns</div>

</main>
</body>
</html>
```